Real Estate Entrepreneur needs a business card

I am a real estate entrepreneur, I buy houses for investment purposes, I act as a real estate agent representing buyers and sellers in residential home transactions, I am a contractor that does a wide range of home repairs and construction. I'd like a design that can stick with me through the years as my business grows and morphs to fit any niche I decide to pursue as markets change.

Target Market(s)

Anyone with interest that may be related to real estate.

Industry/Entity Type

Real Estate

Contact Information for Business Card

A card that stands out and doesn't put me in any one box. My business will evolve over time and I need a card that can stay relevant.

Colors

Designer to choose colors to be used in the design.

Requirements
Must have
• Character
Nice to have
• I'm open
Should not have
• Cliche houses and hammers

```html
<!DOCTYPE html>
<html lang="en">
<head>
<meta charset="utf-8">
<title>Reid Calloway – Business Card</title>
<link href="https://fonts.googleapis.com/css2?family=Montserrat:wght@500;600&family=Roboto+Slab:wght@700&family=Roboto:wght@400&display=swap" rel="stylesheet">
<style>
  :root {
    --backdrop: #d9d9d9;
    --brand-blue: #2ba7df;
    --card-white: #f7f7f7;
    --ink-dark: #3a3a3a;
    --ink-contact: #4a4a4a;
    --monogram-tint: #e8f2f7;
    --front-text: #f3f3f3;
  }
  * { margin: 0; padding: 0; box-sizing: border-box; }
  html, body {
    width: 1078px;
    height: 1200px;
    overflow: hidden;
    background: var(--backdrop);
  }
  .canvas {
    position: relative;
    width: 1078px;
    height: 1200px;
  }
  .card {
    position: absolute;
    left: 190px;
    width: 697px;
    height: 398px;
    overflow: hidden;
  }
  .card--front {
    top: 157px;
    background: var(--brand-blue);
    display: flex;
    align-items: center;
    justify-content: center;
  }
  .front-name {
    font-family: "Montserrat", sans-serif;
    font-weight: 600;
    font-size: 68px;
    letter-spacing: -0.5px;
    color: var(--front-text);
    line-height: 1;
    white-space: nowrap;
  }
  .card--back {
    top: 655px;
    background: var(--card-white);
  }
  .monogram {
    position: absolute;
    right: 47px;
    top: 4px;
    font-family: "Roboto Slab", serif;
    font-weight: 700;
    font-size: 330px;
    line-height: 1;
    color: var(--monogram-tint);
  }
  .identity {
    position: absolute;
    left: 38px;
    top: 38px;
  }
  .identity__name {
    font-family: "Roboto Slab", serif;
    font-weight: 700;
    font-size: 34px;
    line-height: 1;
    color: var(--brand-blue);
    white-space: nowrap;
  }
  .identity__title {
    margin-top: 1px;
    font-family: "Montserrat", sans-serif;
    font-weight: 500;
    font-size: 19px;
    line-height: 1.1;
    color: var(--ink-dark);
  }
  .contact {
    position: absolute;
    left: 379px;
    top: 285px;
    list-style: none;
  }
  .contact__item {
    font-family: "Roboto", sans-serif;
    font-weight: 400;
    font-size: 19px;
    line-height: 25px;
    color: var(--ink-contact);
    white-space: nowrap;
  }
  .contact__label {
    display: inline-block;
    width: 17px;
    font-family: "Roboto Slab", serif;
    font-weight: 700;
    color: var(--brand-blue);
  }
</style>
</head>
<body>
  <main class="canvas">
    <section class="card card--front">
      <h1 class="front-name">REID CALLOWAY</h1>
    </section>

    <section class="card card--back">
      <div class="monogram" aria-hidden="true">R</div>
      <div class="identity">
        <h2 class="identity__name">REID CALLOWAY</h2>
        <p class="identity__title">Business Executive</p>
      </div>
      <ul class="contact">
        <li class="contact__item"><span class="contact__label">P</span> 1300 555 015 (1300 555 015)</li>
        <li class="contact__item"><span class="contact__label">E</span> hello@reidcalloway.com</li>
        <li class="contact__item"><span class="contact__label">w</span> www.reidcalloway.com</li>
      </ul>
    </section>
  </main>
</body>
</html>
```